Closed loop end of life cycle for electronics Loop.

Sustainability Closed Loop. I need six sections on the Closed Loop
1-End-of-life Product & Mfg. Scrap
2-UBNE Services
3-Mechanical Processing
4-Precious Metals Refining
5-Metal Products Manufactured
6-Products return to OEMs
Target Market(s)
Vorex, Norby, KGWR, other major manufacturers of electronics and semiconductor
Industry/Entity Type
Sustainablek
Font styles to use
Serif
Sans Serif
Colors
0054AA
0677BA
7BADD7
CADEEF
E8F1F8
0094D4
00A9DD
6FCCEA
C7EBF8
E9F6FB
00AB8E
00BBA5
67D7C9
C6EFE9
E9F9F6
Requirements
Must have
- Sustainability Closed Loop. I need six sections on the Closed Loop ring below.

```html
<!DOCTYPE html>
<html lang="en">
<head>
<meta charset="utf-8">
<title>Sustainability Closed Loop</title>
<link rel="stylesheet" href="https://fonts.googleapis.com/css2?family=Tinos:ital,wght@1,700&display=swap">
<style>
  :root {
    --canvas-bg: #ffffff;
    --label-ink: #ffffff;
    --title-ink: #000000;
    --green-a: #3fae0a;
    --green-b: #86d05a;
    --red-a: #f0282c;
    --red-b: #fcb0b0;
    --magenta-a: #f526c6;
    --magenta-b: #ee8c9a;
    --purple-a: #6a3590;
    --purple-b: #e4dcf0;
    --blue-a: #6a2cee;
    --blue-b: #48c09a;
    --orange-a: #fbb012;
    --orange-b: #fdd98a;
  }
  html, body {
    margin: 0;
    padding: 0;
    width: 1200px;
    height: 1200px;
    overflow: hidden;
    background: var(--canvas-bg);
  }
  .loop-diagram {
    display: block;
    width: 1200px;
    height: 1200px;
  }
  .stage-label {
    font-family: "Tinos", "Times New Roman", serif;
    font-style: italic;
    font-weight: 700;
    font-size: 66px;
    fill: var(--label-ink);
  }
  .stage-label--compact { font-size: 60px; }
  .loop-title {
    font-family: "Tinos", "Times New Roman", serif;
    font-style: italic;
    font-weight: 700;
    font-size: 128px;
    fill: var(--title-ink);
  }
</style>
</head>
<body>
<svg class="loop-diagram" viewBox="0 0 1920 1920" xmlns="http://www.w3.org/2000/svg">
  <defs>
    <linearGradient id="grad-green" gradientUnits="userSpaceOnUse" x1="400" y1="560" x2="1100" y2="320">
      <stop offset="0" style="stop-color:var(--green-a)"/><stop offset="1" style="stop-color:var(--green-b)"/>
    </linearGradient>
    <linearGradient id="grad-red" gradientUnits="userSpaceOnUse" x1="1040" y1="260" x2="1540" y2="820">
      <stop offset="0" style="stop-color:var(--red-a)"/><stop offset="1" style="stop-color:var(--red-b)"/>
    </linearGradient>
    <linearGradient id="grad-magenta" gradientUnits="userSpaceOnUse" x1="1620" y1="660" x2="1400" y2="1380">
      <stop offset="0" style="stop-color:var(--magenta-a)"/><stop offset="1" style="stop-color:var(--magenta-b)"/>
    </linearGradient>
    <linearGradient id="grad-purple" gradientUnits="userSpaceOnUse" x1="1530" y1="1380" x2="800" y2="1550">
      <stop offset="0" style="stop-color:var(--purple-a)"/><stop offset="1" style="stop-color:var(--purple-b)"/>
    </linearGradient>
    <linearGradient id="grad-blue" gradientUnits="userSpaceOnUse" x1="880" y1="1660" x2="330" y2="1120">
      <stop offset="0" style="stop-color:var(--blue-a)"/><stop offset="1" style="stop-color:var(--blue-b)"/>
    </linearGradient>
    <linearGradient id="grad-orange" gradientUnits="userSpaceOnUse" x1="300" y1="1250" x2="300" y2="560">
      <stop offset="0" style="stop-color:var(--orange-a)"/><stop offset="1" style="stop-color:var(--orange-b)"/>
    </linearGradient>

    <path id="arc-green-1" d="M398.1 1222 A620 620 0 0 1 1521.9 698"/>
    <path id="arc-green-2" d="M470.6 1188.2 A540 540 0 0 1 1449.4 731.8"/>
    <path id="arc-red-1" d="M447.8 559.8 A650 650 0 0 1 1472.2 1360.2"/>
    <path id="arc-red-2" d="M495.1 596.7 A590 590 0 0 1 1424.9 1323.3"/>
    <path id="arc-red-3" d="M542.4 633.7 A530 530 0 0 1 1377.6 1286.3"/>
    <path id="arc-magenta-1" d="M989.8 390.8 A570 570 0 0 1 930.2 1529.2"/>
    <path id="arc-purple-1" d="M1512.4 678.5 A620 620 0 0 1 407.6 1241.5"/>
    <path id="arc-purple-2" d="M1441.1 714.8 A540 540 0 0 1 478.9 1205.2"/>
    <path id="arc-blue-1" d="M1480 1297.7 A620 620 0 0 1 440 622.3"/>
    <path id="arc-blue-2" d="M1412.9 1254.1 A540 540 0 0 1 507.1 665.9"/>
    <path id="arc-orange-1" d="M927.6 1579.1 A620 620 0 0 1 992.4 340.9"/>
    <path id="arc-orange-2" d="M931.8 1499.2 A540 540 0 0 1 988.2 420.8"/>
  </defs>

  <g class="ring-bands">
    <path class="band band--green" fill="url(#grad-green)" d="M360.3 570.6 A715 715 0 0 1 960 245 L960 495 A465 465 0 0 0 570 706.8 Z"/>
    <path class="band band--red" fill="url(#grad-red)" d="M997.4 246 A715 715 0 0 1 1579.2 602.5 L1362.7 727.5 A465 465 0 0 0 984.3 495.7 Z"/>
    <path class="band band--magenta" fill="url(#grad-magenta)" d="M1597.1 635.4 A715 715 0 0 1 1579.2 1317.5 L1362.7 1192.5 A465 465 0 0 0 1374.3 748.9 Z"/>
    <path class="band band--purple" fill="url(#grad-purple)" d="M1559.7 1349.4 A715 715 0 0 1 960 1675 L960 1425 A465 465 0 0 0 1350 1213.2 Z"/>
    <path class="band band--blue" fill="url(#grad-blue)" d="M922.6 1674 A715 715 0 0 1 340.8 1317.5 L557.3 1192.5 A465 465 0 0 0 935.7 1424.3 Z"/>
    <path class="band band--orange" fill="url(#grad-orange)" d="M322.9 1284.6 A715 715 0 0 1 340.8 602.5 L557.3 727.5 A465 465 0 0 0 545.7 1171.1 Z"/>
  </g>

  <g class="ring-arrowheads">
    <path class="arrowhead arrowhead--green" fill="url(#grad-green)" d="M960 190 L1132.5 395.8 L960 595 Z"/>
    <path class="arrowhead arrowhead--red" fill="url(#grad-red)" d="M1626.8 575 L1534.9 827.2 L1276.1 777.5 Z"/>
    <path class="arrowhead arrowhead--magenta" fill="url(#grad-magenta)" d="M1626.8 1345 L1362.4 1391.5 L1276.1 1142.5 Z"/>
    <path class="arrowhead arrowhead--purple" fill="url(#grad-purple)" d="M960 1730 L787.5 1524.2 L960 1325 Z"/>
    <path class="arrowhead arrowhead--blue" fill="url(#grad-blue)" d="M293.2 1345 L385.1 1092.8 L643.9 1142.5 Z"/>
    <path class="arrowhead arrowhead--orange" fill="url(#grad-orange)" d="M293.2 575 L557.6 528.5 L643.9 777.5 Z"/>
  </g>

  <g class="stage-labels">
    <text class="stage-label"><textPath href="#arc-green-1" startOffset="50%" text-anchor="middle">Products return</textPath></text>
    <text class="stage-label"><textPath href="#arc-green-2" startOffset="50%" text-anchor="middle">to OEMs</textPath></text>

    <text class="stage-label stage-label--compact"><textPath href="#arc-red-1" startOffset="50%" text-anchor="middle">End-of-life</textPath></text>
    <text class="stage-label stage-label--compact"><textPath href="#arc-red-2" startOffset="50%" text-anchor="middle">Product &amp;</textPath></text>
    <text class="stage-label stage-label--compact"><textPath href="#arc-red-3" startOffset="50%" text-anchor="middle">Mfg. Scrap</textPath></text>

    <text class="stage-label"><textPath href="#arc-magenta-1" startOffset="50%" text-anchor="middle">UBNE Services</textPath></text>

    <text class="stage-label"><textPath href="#arc-purple-1" startOffset="50%" text-anchor="middle">Mechanical</textPath></text>
    <text class="stage-label"><textPath href="#arc-purple-2" startOffset="50%" text-anchor="middle">Processing</textPath></text>

    <text class="stage-label"><textPath href="#arc-blue-1" startOffset="50%" text-anchor="middle">Precious Metals</textPath></text>
    <text class="stage-label"><textPath href="#arc-blue-2" startOffset="50%" text-anchor="middle">Refining</textPath></text>

    <text class="stage-label"><textPath href="#arc-orange-1" startOffset="50%" text-anchor="middle">Metal Products</textPath></text>
    <text class="stage-label"><textPath href="#arc-orange-2" startOffset="50%" text-anchor="middle">Manufactured</textPath></text>
  </g>

  <g class="loop-titles" text-anchor="middle">
    <text class="loop-title" x="960" y="918">Sustainability</text>
    <text class="loop-title" x="960" y="1080">Closed</text>
    <text class="loop-title" x="960" y="1242">Loop</text>
  </g>
</svg>
</body>
</html>
```